Business card design for international hub site

I need a business card design with the logo attached. Although the site is for the teenage audience (it is about the high school graduation ball, the Prom), the business card is for professional use to be given to professional contacts (B2B), such as suppliers and partners, so it needs to look professional (but also girly, glamours and clean).

Target Market(s)

B2B

Industry/Entity Type

Media

Colors
eea4c8
f9d9e8
e667a6
9d9d9d
1b1b1b

Requirements
Must have
• Space for Name, Tile, Address, Phone, email and website.
Should not have
• Photo

```html
<!DOCTYPE html>
<html lang="en">
<head>
<meta charset="utf-8">
<title>Gala Glow – Business Card</title>
<link href="https://fonts.googleapis.com/css2?family=EB+Garamond:wght@400;600&family=Pinyon+Script&display=swap" rel="stylesheet">
<style>
  :root {
    --page-bg: #f2f2f2;
    --card-dark: #2a2a2a;
    --card-darker: #1b1b1b;
    --card-light: #333333;
    --ink-white: #ffffff;
    --ink-soft: #e6e6e6;
    --accent-pink: #e667a6;
    --accent-pink-light: #eea4c8;
  }
  * { margin: 0; padding: 0; box-sizing: border-box; }
  html, body {
    width: 1200px;
    height: 586px;
    overflow: hidden;
    background: var(--page-bg);
    font-family: "EB Garamond", Georgia, serif;
  }
  .canvas {
    position: relative;
    width: 1200px;
    height: 586px;
  }
  .card {
    position: absolute;
    top: 129px;
    width: 502px;
    height: 301px;
    overflow: hidden;
  }
  .card--front { left: 65px; }
  .card--back { left: 608px; }
  .card__texture {
    position: absolute;
    inset: 0;
    background:
      linear-gradient(125deg, var(--card-light) 0%, var(--card-dark) 35%, var(--card-darker) 60%, var(--card-dark) 85%, var(--card-light) 100%);
  }

  /* Front */
  .brand-name {
    position: absolute;
    left: 0;
    right: 0;
    top: 92px;
    text-align: center;
    color: var(--ink-white);
    font-size: 62px;
    font-weight: 400;
    line-height: 1;
    letter-spacing: 1px;
  }
  .brand-name__dot {
    display: inline-block;
    width: 10px;
    height: 10px;
    border-radius: 50%;
    background: var(--ink-white);
    margin-left: 10px;
    vertical-align: middle;
  }
  .website {
    position: absolute;
    left: 0;
    right: 0;
    top: 258px;
    text-align: center;
    color: var(--ink-white);
    font-size: 12px;
    font-weight: 600;
    letter-spacing: 3.6px;
  }

  /* Back */
  .person-name {
    position: absolute;
    left: 56px;
    top: 134px;
    color: var(--ink-white);
    font-family: "Pinyon Script", cursive;
    font-size: 33px;
    line-height: 1;
  }
  .divider {
    position: absolute;
    left: 251px;
    top: 84px;
    width: 3px;
    height: 142px;
    background: linear-gradient(to bottom, rgba(230,103,166,0) 0%, var(--accent-pink) 30%, var(--accent-pink) 65%, rgba(230,103,166,0) 100%);
  }
  .contact-list {
    position: absolute;
    left: 277px;
    top: 121px;
    list-style: none;
  }
  .contact-list__item {
    display: flex;
    align-items: center;
    height: 24px;
    color: var(--ink-soft);
    font-size: 13px;
  }
  .contact-list__icon {
    width: 14px;
    height: 12px;
    margin-right: 8px;
    fill: var(--accent-pink);
  }
  .address {
    position: absolute;
    left: 0;
    right: 0;
    top: 270px;
    text-align: center;
    color: var(--accent-pink);
    font-size: 14.5px;
    font-weight: 600;
  }
</style>
</head>
<body>
<main class="canvas">

  <section class="card card--front" aria-label="Business card front">
    <div class="card__texture" role="img" aria-label="Dark faceted geometric background"></div>
    <h1 class="brand-name">gala glow<span class="brand-name__dot"></span></h1>
    <p class="website">www.galaglow.com</p>
  </section>

  <section class="card card--back" aria-label="Business card back">
    <div class="card__texture" role="img" aria-label="Dark faceted geometric background"></div>
    <p class="person-name">Mara Ellison</p>
    <div class="divider"></div>
    <ul class="contact-list">
      <li class="contact-list__item">
        <svg class="contact-list__icon" viewBox="0 0 14 12" aria-hidden="true">
          <path d="M1 3.5 C1 1.5 4 0.5 7 0.5 S13 1.5 13 3.5 L13 4.5 L10 4.5 L10 3 L4 3 L4 4.5 L1 4.5 Z"/>
          <path d="M4 5 L10 5 L12.5 8 L12.5 11.5 L1.5 11.5 L1.5 8 Z"/>
        </svg>
        +44 (0)1632 960481
      </li>
      <li class="contact-list__item">
        <svg class="contact-list__icon" viewBox="0 0 14 12" aria-hidden="true">
          <rect x="3.5" y="0.5" width="7" height="3.5"/>
          <path d="M0.5 4.5 H13.5 V9.5 H11 V7.5 H3 V9.5 H0.5 Z"/>
          <rect x="3.5" y="8.5" width="7" height="3"/>
        </svg>
        (555) 014-2290
      </li>
      <li class="contact-list__item">
        <svg class="contact-list__icon" viewBox="0 0 14 12" aria-hidden="true">
          <path d="M0.5 1.5 H13.5 V10.5 H0.5 Z M1.5 2.5 L7 7 L12.5 2.5 Z" fill-rule="evenodd"/>
        </svg>
        mara@galaglow.com
      </li>
    </ul>
    <p class="address">Elm Court, Westbury Vale, YO9 4QD</p>
  </section>

</main>
</body>
</html>
```